Uitnodiging van het huwelijk
doelgroep
Uitnodiging voor onze bruiloft voor vrienden en familie
Conceptuele formulering
Wij willen hutten individuele uitnodigingskaart. Het moet iets bijzonders zijn, dwz straalt iets bijzonders, maar anders vrij eenvoudig en modern en niet cheesy! Op de voorkant van onze huwelijksdatum en onze namen moeten eventueel een foto van ons. misschien zelfs een citaat: "Het geluk is het enige dat verdubbelt als je het (Gustav Mellinger) Uitnodiging voor onze kerk bruiloft misschien een motief, wat doe je het citaat past delen ....

```html
<!DOCTYPE html>
<html lang="de">
<head>
<meta charset="utf-8">
<title>Hochzeitseinladung Marlene &amp; Tobias</title>
<link rel="stylesheet" href="https://fonts.googleapis.com/css2?family=Grand+Hotel&family=Pathway+Gothic+One&display=swap">
<style>
  :root {
    --paper: #ffffff;
    --backdrop: #ffffff;
    --accent-red: #b5132e;
    --ink-grey: #7d7d7d;
    --body-grey: #555555;
    --photo-grey: #e8e9e8;
    --ornament-grey: #d2d2d2;
    --card-shadow: 0 1px 3px rgba(0,0,0,0.22);
  }
  * { margin: 0; padding: 0; box-sizing: border-box; }
  html, body {
    width: 1200px; height: 848px; overflow: hidden;
    background: var(--backdrop);
  }
  .canvas { position: relative; width: 1200px; height: 848px; }

  .card {
    position: absolute;
    background: var(--paper);
    box-shadow: var(--card-shadow);
    overflow: hidden;
    text-align: center;
  }
  .script { font-family: "Grand Hotel", cursive; color: var(--accent-red); }
  .sans { font-family: "Pathway Gothic One", sans-serif; }

  .ornament {
    position: absolute;
    background: radial-gradient(ellipse at center, var(--ornament-grey) 0%, rgba(210,210,210,0.45) 45%, rgba(255,255,255,0) 72%);
  }

  /* Front card */
  .front { left: 60px; top: 40px; width: 340px; height: 330px; }
  .front .kicker {
    position: absolute; top: 42px; left: 0; right: 0;
    font-family: "Grand Hotel", cursive; color: var(--ink-grey); font-size: 19px;
  }
  .front .couple {
    position: absolute; top: 62px; left: 0; right: 0;
    font-size: 44px; line-height: 1;
  }
  .front .date {
    position: absolute; top: 118px; left: 0; right: 0;
    color: var(--ink-grey); font-size: 15px;
  }
  .front .heart { position: absolute; top: 144px; left: 159px; width: 24px; height: 22px; }
  .front .quote {
    position: absolute; top: 178px; left: 0; right: 0;
    font-size: 12.5px; line-height: 1.32;
  }
  .attribution {
    display: block; font-family: "Pathway Gothic One", sans-serif;
    font-size: 6.5px; margin-top: 4px; color: var(--accent-red);
  }
  .front .orn-left { left: -30px; top: 250px; width: 240px; height: 110px; }
  .front .orn-right { left: 260px; top: 200px; width: 110px; height: 150px; }

  /* Inner spread */
  .spread { left: 136px; top: 395px; width: 636px; height: 318px; text-align: center; }
  .panel { position: absolute; top: 0; width: 318px; height: 318px; }
  .panel-left { left: 0; }
  .panel-right { left: 318px; border-left: 1px solid #eeeeee; }
  .photo-slot { position: absolute; background: var(--photo-grey); }
  .panel-left .orn-top { left: -20px; top: -30px; width: 230px; height: 120px; }
  .panel-left .song {
    position: absolute; top: 96px; left: 0; right: 0;
    font-size: 12.5px; line-height: 1.22;
  }
  .panel-right .headline {
    position: absolute; top: 110px; left: 0; right: 0;
    font-size: 21px;
  }
  .panel-right .invitation {
    position: absolute; top: 140px; left: 0; right: 0;
    color: var(--body-grey); font-size: 10px; line-height: 1.22;
  }
  .invitation p { margin-bottom: 6px; }
  .panel-right .signature {
    position: absolute; top: 262px; left: 0; right: 0;
    font-size: 27px; word-spacing: 10px;
  }
  .panel-right .orn-corner { left: 250px; top: 210px; width: 90px; height: 120px; }

  /* Back card */
  .back { left: 810px; top: 474px; width: 336px; height: 330px; }
  .back .orn-top { left: -20px; top: -30px; width: 380px; height: 130px; }
  .back .orn-corner { left: 250px; top: 210px; width: 100px; height: 130px; }
  .back .poem {
    position: absolute; top: 104px; left: 0; right: 0;
    font-size: 12px; line-height: 1.35;
  }
  .poem p { margin-bottom: 6px; }
  .back .notes {
    position: absolute; top: 270px; left: 20px; right: 60px;
    text-align: left; color: var(--body-grey); font-size: 7px; line-height: 1.3;
  }
  .notes p { margin-bottom: 5px; }
</style>
</head>
<body>
<div class="canvas">

  <section class="card front">
    <div class="ornament orn-left" role="img" aria-label="Graue Ranken-Ornamente unten links"></div>
    <div class="ornament orn-right" role="img" aria-label="Graue Ranken-Ornamente unten rechts"></div>
    <div class="kicker">Wir heiraten</div>
    <h1 class="couple script">Marlene &amp; Tobias</h1>
    <div class="date sans">20. Juli 2013</div>
    <svg class="heart" viewBox="0 0 24 22" aria-hidden="true">
      <path d="M12 21 C5 15 0 11 0 6 C0 2.5 2.7 0 6 0 C8.6 0 10.7 1.6 12 3.8 C13.3 1.6 15.4 0 18 0 C21.3 0 24 2.5 24 6 C24 11 19 15 12 21 Z" fill="var(--accent-red)"/>
    </svg>
    <p class="quote script">Das Glück<br>ist das Einzige,<br>das sich verdoppelt,<br>wenn man es teilt.
      <span class="attribution">(Gustav Mellinger)</span></p>
  </section>

  <section class="card spread">
    <div class="panel panel-left">
      <div class="ornament orn-top" role="img" aria-label="Graue Ranken-Ornamente oben links"></div>
      <p class="song script">„Ja“ zu jedem Tag mit Dir.<br>„Ja“ zu jedem Deiner Fehler.<br>Asche und Geld, ich trag’ alles mit Dir.<br>Denn ich bin und bleib verlor’n in Deiner Mitte.<br>In Deiner Mitte, bis der Vorhang fällt!
        <span class="attribution">(„Ja“ von Nachtfalter)</span></p>
      <div class="photo-slot" style="left:0;top:222px;width:94px;height:84px"></div>
      <div class="photo-slot" style="left:109px;top:222px;width:97px;height:84px"></div>
      <div class="photo-slot" style="left:221px;top:222px;width:97px;height:84px"></div>
    </div>
    <div class="panel panel-right">
      <div class="photo-slot" style="left:0;top:11px;width:96px;height:86px"></div>
      <div class="photo-slot" style="left:111px;top:11px;width:96px;height:86px"></div>
      <div class="photo-slot" style="left:222px;top:11px;width:96px;height:86px"></div>
      <div class="ornament orn-corner" role="img" aria-label="Graue Ranken-Ornamente unten rechts"></div>
      <h2 class="headline script">Wir sagen „Ja“ zueinander!</h2>
      <div class="invitation sans">
        <p>Was wir letztes Jahr beim Standesamt begonnen haben, möchten wir<br>mir allen unseren Freunden und Verwandten vor dem Traualter vollenden.</p>
        <p>Wir laden daher herzlich zu unserer kirchlichen Trauung mit<br>anschließender Feier im Seehotel Lindenau ein.</p>
        <p>Die Hochzeitsglocken der katholischen Kirche St. Laurentius,<br>in Grünwiesen, läuten für uns um 14:00 Uhr.</p>
        <p>Bitte gebt uns bis spätestens 26. April 2013 Bescheid.</p>
        <p>Wir freuen uns auf Dich/Euch und einen wundervollen Tag!</p>
      </div>
      <div class="signature script">Marlene Tobias</div>
    </div>
  </section>

  <section class="card back">
    <div class="ornament orn-top" role="img" aria-label="Graue Ranken-Ornamente am oberen Rand"></div>
    <div class="ornament orn-corner" role="img" aria-label="Graue Ranken-Ornamente unten rechts"></div>
    <div class="poem script">
      <p>Liebe Gäste lasst Euch sagen,<br>Pakete braucht Ihr nicht zu tragen.</p>
      <p>Auch braucht Ihr nicht zu laufen,<br>um Geschenke einzukaufen.</p>
      <p>Denn unser Haushalt der ist voll,<br>drum fänden wir es richtig toll,<br>ein Kuvert mit etwas drin,<br>macht uns Freude und hat Sinn.</p>
    </div>
    <div class="notes sans">
      <p>Solltet Ihr unseren besonderen Tag mit netten Überraschungen mitgestalten wollen, so wendet Euch bitte rechtzeitig an: Helene Brandt, Telefon: 0171.5550123.</p>
      <p>Für Zimmerbuchungen: Seehotel Lindenau, Telefon: 06021.555-0, www.seehotel-lindenau.de</p>
    </div>
  </section>

</div>
</body>
</html>
```